Orra Leave In Conditioning Mist

The product is a 10oz light detangler in a continuous mister bottle. Trying to be an alternative to a competitor, "Brindle Hush Satin Spray" https://brindlehushhairco.com/products/satin-spray-leave-in-conditioner

The brand name is "Orra" or "ORRA".
Product is a "10 in 1 Multi-Use Leave In Conditioner (zing veil)"
Featured ingredient is "Biotin" and "Keratin"

The art attached shows my attempt but it needs to be classier.

Label size is 6.75"W x 5.25"H (rounded edges).
Material is silver foil with matte finish overlay.

Thank you,
Dale

Orra

```html
<!DOCTYPE html>
<html lang="en">
<head>
<meta charset="utf-8">
<title>Orra Leave In Conditioning Mist – Labels</title>
<link href="https://fonts.googleapis.com/css2?family=Montserrat:wght@300;400;500;600;700&family=Oswald:wght@300;400&display=swap" rel="stylesheet">
<style>
  :root{
    --page:#ffffff;
    --tan-a:#d6ab84;
    --tan-b:#efd9c4;
    --tan-c:#fbf3ec;
    --white:#ffffff;
  }
  *{box-sizing:border-box;margin:0;padding:0}
  html,body{width:1200px;height:1051px;overflow:hidden;background:var(--page)}
  body{position:relative;font-family:"Montserrat",sans-serif}

  .label{position:absolute;left:311px;width:578px;height:464px;background:var(--bg);overflow:hidden}
  .label--biotin{top:50px;--bg:#3dbbea;--ink:#27287f;--soft:#7fd3f3;--frame:#e9a4c6}
  .label--keratin{top:536px;--bg:#ee6aa6;--ink:#c2195c;--soft:#f6a3c8;--frame:#e7c7a0}

  .label__frame{position:absolute;left:8px;top:13px;width:562px;height:438px;border:1px solid var(--frame);border-radius:18px}

  /* back panel copy */
  .info{position:absolute;left:31px;top:32px;width:145px;color:var(--ink);font-size:6.3px;line-height:7.8px;font-weight:300}
  .info p{text-align:justify}
  .info h4{font-size:7.6px;font-weight:600;line-height:9px;margin-top:9px}
  .info__made{font-size:7.6px;font-weight:600;margin-top:9px}
  .distrib{position:absolute;left:31px;top:349px;color:var(--white);font-size:6.3px;line-height:7.6px;font-weight:300}
  .distrib b{font-weight:600}
  .barcode-space{position:absolute;left:31px;top:387px;width:95px;height:47px;background:var(--white)}
  .peel{position:absolute;left:127px;top:341px;width:50px;height:50px;border-radius:50%;background:radial-gradient(circle at 35% 35%,var(--tan-c),var(--tan-b) 55%,var(--tan-a));display:flex;align-items:center;justify-content:center;text-align:center;color:var(--ink);font-size:7px;line-height:7.6px;transform:rotate(-8deg)}
  .label--keratin .peel{font-weight:700;font-size:6px;text-transform:uppercase}
  .care-icons{position:absolute;left:131px;top:410px}

  /* front panel */
  .brandband{position:absolute;left:284px;top:6px;width:292px;height:71px;background:linear-gradient(90deg,var(--tan-a),var(--tan-b) 55%,var(--tan-c) 90%,var(--white))}
  .brandband__name{position:absolute;left:7px;top:17px;font-family:"Montserrat",sans-serif;font-weight:700;font-size:54px;line-height:54px;letter-spacing:12px;color:var(--white);white-space:nowrap}
  .brandband__rule{position:absolute;left:284px;top:80px;width:292px;height:3px;background:var(--white)}
  .brandband__bar{position:absolute;left:281px;top:88px;width:295px;height:12px;background:var(--ink)}

  .tagline{position:absolute;left:254px;top:32px;height:404px;width:26px;writing-mode:vertical-rl;transform:rotate(180deg);font-size:21px;letter-spacing:1.6px;color:var(--soft);text-align:center;white-space:nowrap;line-height:26px}

  .title{position:absolute;left:290px;font-family:"Oswald",sans-serif;white-space:nowrap;transform-origin:left top}
  .title--count{top:113px;font-size:29px;line-height:29px;font-weight:300;color:var(--ink);letter-spacing:2.5px}
  .title--multi{top:144px;font-size:25px;line-height:25px;font-weight:300;color:var(--white);transform:scaleY(1.2)}
  .title--main{top:170px;font-size:44px;line-height:44px;font-weight:400;color:var(--white);transform:scaleY(1.15)}
  .formula{position:absolute;left:289px;top:225px;width:223px;height:25px;background:linear-gradient(90deg,var(--tan-a),var(--tan-b));color:var(--white);font-size:14.4px;font-weight:500;line-height:25px;padding-left:8px;white-space:nowrap}

  .badges{position:absolute;left:284px;top:284px;width:233px;height:31px;background:var(--ink);display:flex;align-items:center;padding-left:4px;gap:6px}
  .badge{display:flex;align-items:center;gap:4px;color:var(--white);font-size:9.2px;line-height:10px;font-weight:500;width:72px}
  .badge svg{flex:none}

  .benefits{position:absolute;left:291px;top:319px;display:grid;grid-template-columns:78px 120px;row-gap:4.6px;color:var(--white);font-size:11.8px;font-weight:300;list-style:none}
  .benefits li{position:relative;padding-left:9px;line-height:14px;white-space:nowrap}
  .benefits li::before{content:"";position:absolute;left:0;top:5px;width:4px;height:4px;border-radius:50%;background:var(--tan-b)}
  .volume{position:absolute;left:290px;top:421px;color:var(--white);font-size:12.5px;line-height:16px;font-weight:400}
</style>
</head>
<body>

<section class="label label--biotin" aria-label="Orra biotin leave in mist label">
  <div class="label__frame"></div>
  <div class="info">
    <p>Helps reduce brassiness or unwanted yellow tones. Our professional pigmented formula utilizes principles of color theory, neutralizing and contracting unwanted hues, leaving brightened, hydrated, and softer hair.</p>
    <div class="info__made">Made in Los Angeles, CA</div>
    <h4>Our Promise</h4>
    <p>We never use parabens to preserve, harmful phthalate fragrance, ingredients tested on animals, or chemicals harmful to the environment &amp; skin.</p>
    <h4>Direction Of Use</h4>
    <p>Apply throughout towel dried hair. Starting from roots to ends. Comb through. Do not wash out. Apply as needed. Style as usual. Heat &amp; Color-Safe.</p>
    <h4>Ingredients</h4>
    <p>Water (Aqua), Butylene Glycol, Cetyl Alcohol, Stearyl Alcohol, Behentrimonium Chloride, Centrimonium Chloride, Biotin, Hydrolyzed Keratin, Fragrance (Parfum), Hydrolyzed Rice Protein, Adansonia Digitata Seed Extract, Amaranthus Caudatus Seed Extract, Hydrolyzed Vegetable Protein, Pg-Propyl Silanetriol, Crambe Maritima (Blue Sea Kale) Leaf Extract, Chlorella Pyrenoidosa Extract, Chondrus Crispus (Carrageenan) Extract, Undaria Pinnatifida Extract, Laminaria Saccharina Extract, Ethylhexylglycerin, Phenoxyethanol, Anise Alcohol, Benzyl Benzoate, Butylphenyl Methylpropional, Cinnamyl Alcohol, Coumarin, Eugenol, Geraniol, Hexyl Cinnamal, Limonene</p>
  </div>
  <div class="distrib"><b>Distributed by</b><br>Fernwick Goods LLC<br>Harbor Vale, FL 30000<br>fernwickgoods.com<br>ORRWM12</div>
  <div class="peel">Peel Off<br>Label &amp;<br>Reuse<br>Bottle!</div>
  <div class="barcode-space"></div>
  <svg class="care-icons" width="46" height="24" viewBox="0 0 46 24" fill="none" stroke="#fff" stroke-width="1.2">
    <path d="M2 10h14v11H2z"/><path d="M1 8l14-5 1 3-14 5z"/><text x="5" y="19" font-size="5" fill="#fff" stroke="none" font-family="Montserrat,sans-serif">12M</text>
    <path d="M30 6l4-4 4 4M42 12l1 6h-6M26 14l-2 5h7"/><path d="M34 2v8M43 18l-5-5M24 19l5-6"/>
  </svg>

  <div class="tagline">BRIGHTEN – REVIVE – EVERYDAY</div>
  <div class="brandband"><span class="brandband__name">ORRA</span></div>
  <div class="brandband__rule"></div>
  <div class="brandband__bar"></div>

  <div class="title title--count">10-IN-1</div>
  <div class="title title--multi">MULTI-USE</div>
  <div class="title title--main">LEAVE IN MIST</div>
  <div class="formula">BIOTIN INFUSED FORMULA</div>

  <div class="badges">
    <div class="badge"><svg width="20" height="20" viewBox="0 0 20 20" fill="none" stroke="#fff" stroke-width="1"><circle cx="10" cy="10" r="9"/><path d="M5 8h8v3H5zM13 9h2M8 11l-1 4"/></svg>Salon<br>Formula</div>
    <div class="badge"><svg width="20" height="20" viewBox="0 0 20 20" fill="none" stroke="#fff" stroke-width="1"><circle cx="10" cy="10" r="9"/><circle cx="10" cy="10" r="5"/><circle cx="10" cy="10" r="2"/></svg>Sulfate<br>Free</div>
    <div class="badge"><svg width="20" height="20" viewBox="0 0 20 20" fill="none" stroke="#fff" stroke-width="1"><circle cx="10" cy="10" r="9"/><path d="M10 4c-3 4-3 6 0 8 3-2 3-4 0-8zM10 12v4"/></svg>Paraben<br>Free</div>
  </div>

  <ul class="benefits">
    <li>Moisturize</li><li>Split Ends</li>
    <li>Detangle</li><li>Frizz Control</li>
    <li>Breakage</li><li>Smooth Cuticle</li>
    <li>Shine</li><li>Strengthen Shine</li>
    <li>Hydrate</li><li>UV Protection</li>
  </ul>
  <div class="volume">10oz / 295mL</div>
</section>

<section class="label label--keratin" aria-label="Orra keratin leave in mist label">
  <div class="label__frame"></div>
  <div class="info">
    <p>Helps reduce brassiness or unwanted yellow tones. Our professional pigmented formula utilizes principles of color theory, neutralizing and contracting unwanted hues, leaving brightened, hydrated, and softer hair.</p>
    <div class="info__made">Made in Los Angeles, CA</div>
    <h4>Our Promise</h4>
    <p>We never use parabens to preserve, harmful phthalate fragrance, ingredients tested on animals, or chemicals harmful to the environment &amp; skin.</p>
    <h4>Direction Of Use</h4>
    <p>Apply throughout towel dried hair. Starting from roots to ends. Comb through. Do not wash out. Apply as needed. Style as usual. Heat &amp; Color-Safe.</p>
    <h4>Ingredients</h4>
    <p>Water (Aqua), Butylene Glycol, Cetyl Alcohol, Stearyl Alcohol, Behentrimonium Chloride, Centrimonium Chloride, Biotin, Hydrolyzed Keratin, Fragrance (Parfum), Hydrolyzed Rice Protein, Adansonia Digitata Seed Extract, Amaranthus Caudatus Seed Extract, Hydrolyzed Vegetable Protein, Pg-Propyl Silanetriol, Crambe Maritima (Blue Sea Kale) Leaf Extract, Chlorella Pyrenoidosa Extract, Chondrus Crispus (Carrageenan) Extract, Undaria Pinnatifida Extract, Laminaria Saccharina Extract, Ethylhexylglycerin, Phenoxyethanol, Anise Alcohol, Benzyl Benzoate, Butylphenyl Methylpropional, Cinnamyl Alcohol, Coumarin, Eugenol, Geraniol, Hexyl Cinnamal, Limonene</p>
  </div>
  <div class="distrib"><b>Distributed by</b><br>Fernwick Goods LLC<br>Harbor Vale, FL 30000<br>fernwickgoods.com<br>ORRWM12</div>
  <div class="peel">Peel Off<br>Label &amp;<br>Reuse<br>Bottle!</div>
  <div class="barcode-space"></div>
  <svg class="care-icons" width="46" height="24" viewBox="0 0 46 24" fill="none" stroke="#fff" stroke-width="1.2">
    <path d="M2 10h14v11H2z"/><path d="M1 8l14-5 1 3-14 5z"/><text x="5" y="19" font-size="5" fill="#fff" stroke="none" font-family="Montserrat,sans-serif">12M</text>
    <path d="M30 6l4-4 4 4M42 12l1 6h-6M26 14l-2 5h7"/><path d="M34 2v8M43 18l-5-5M24 19l5-6"/>
  </svg>

  <div class="tagline">BRIGHTEN – REVIVE – EVERYDAY</div>
  <div class="brandband"><span class="brandband__name">ORRA</span></div>
  <div class="brandband__rule"></div>
  <div class="brandband__bar"></div>

  <div class="title title--count">10-IN-1</div>
  <div class="title title--multi">MULTI-USE</div>
  <div class="title title--main">LEAVE IN MIST</div>
  <div class="formula">KERATIN NFUSED FORMULA</div>

  <div class="badges">
    <div class="badge"><svg width="20" height="20" viewBox="0 0 20 20" fill="none" stroke="#fff" stroke-width="1"><circle cx="10" cy="10" r="9"/><path d="M5 8h8v3H5zM13 9h2M8 11l-1 4"/></svg>Salon<br>Formula</div>
    <div class="badge"><svg width="20" height="20" viewBox="0 0 20 20" fill="none" stroke="#fff" stroke-width="1"><circle cx="10" cy="10" r="9"/><circle cx="10" cy="10" r="5"/><circle cx="10" cy="10" r="2"/></svg>Sulfate<br>Free</div>
    <div class="badge"><svg width="20" height="20" viewBox="0 0 20 20" fill="none" stroke="#fff" stroke-width="1"><circle cx="10" cy="10" r="9"/><path d="M10 4c-3 4-3 6 0 8 3-2 3-4 0-8zM10 12v4"/></svg>Paraben<br>Free</div>
  </div>

  <ul class="benefits">
    <li>Moisturize</li><li>Split Ends</li>
    <li>Detangle</li><li>Frizz Control</li>
    <li>Breakage</li><li>Smooth Cuticle</li>
    <li>Shine</li><li>Strengthen Shine</li>
    <li>Hydrate</li><li>UV Protection</li>
  </ul>
  <div class="volume">10oz / 295mL</div>
</section>

</body>
</html>
```